Generic fund comparison

We need a power point template to be used for presentation decks and proposals to clients and prospects. We are an independent Registered Investment Advisor in Pittsburgh Pennsylvania.
Our services include family office, alternative investments, investment management, financial planning and consulting.
We would like to see designs that use the color green and grey as they are part of our logo and brand image. The final design should communicate our guiding principles: 'educate, plan, implement, adapt'

```html
<!DOCTYPE html>
<html lang="en">
<head>
<meta charset="utf-8">
<title>Vanterra – Presentation Template</title>
<link rel="stylesheet" href="https://fonts.googleapis.com/css2?family=Raleway:wght@500;600;700&family=Open+Sans:ital,wght@0,400;0,600;0,700;1,600&display=swap">
<style>
:root{
  --green:#8dc63f;
  --green-dark:#5f8f22;
  --grey:#6f6f70;
  --ink:#1e1e1e;
  --text:#4a4a4a;
  --canvas:#d7d7d7;
  --paper:#ffffff;
  --cell-green:#c6efce;
  --cell-pink:#ffc7ce;
  --cell-grey:#e8e8e8;
  --grid:#e4e4e4;
  --line-blue:#2e75b6;
  --line-bench:#4e7d2e;
  --line-yellow:#f2b632;
  --line-orange:#ed7d31;
  --line-greybar:#a5a5a5;
}
*{box-sizing:border-box;margin:0;padding:0}
html,body{width:1200px;height:3386px;overflow:hidden;background:var(--canvas)}
body{font-family:"Open Sans",Arial,sans-serif;color:var(--text)}
.deck{
  width:1200px;height:3386px;padding:10px;
  display:grid;grid-template-columns:585px 585px;column-gap:10px;
  grid-template-rows:repeat(10,329px);row-gap:8.44px;
}
.slide{position:relative;width:585px;height:329px;overflow:hidden;background:var(--paper)}
.slide--grey{background:var(--grey)}
.slide--green{background:var(--green)}
.fill{position:absolute;inset:0;width:585px;height:329px}

.lockup{position:absolute;display:flex;flex-direction:column;align-items:flex-start;gap:6px}
.lockup--center{align-items:center;left:0;right:0}
.lockup__mark{width:14px;height:14px;background:var(--green)}
.lockup__name{font-family:"Raleway",sans-serif;font-weight:700;font-size:13px;letter-spacing:.5px;color:var(--grey)}
.slide--grey .lockup__name{color:#fff}

.cover-title{position:absolute;font-family:"Raleway",sans-serif;font-weight:700;color:#fff}
.cover-title--dark{color:var(--grey)}
.cover-date{position:absolute;font-size:10px;color:#fff}
.cover-date--dark{color:var(--grey)}
.brand-block{position:absolute}
.bar-bottom{position:absolute;left:0;right:0;bottom:0;height:7px;background:var(--green)}
.bar-top{position:absolute;left:0;right:0;top:0;height:6px;background:var(--green)}

.corner-mark{position:absolute;left:10px;top:9px;width:14px;height:14px;background:var(--green)}
.confidential{position:absolute;left:22px;top:90px;height:150px;writing-mode:vertical-rl;transform:rotate(180deg);font-size:5.5px;color:#9a9a9a;text-align:center}
.page-no{position:absolute;left:10px;bottom:8px;width:13px;height:13px;background:var(--green);color:#fff;font-size:6px;font-weight:700;display:flex;align-items:center;justify-content:center}
.slide-title{position:absolute;left:45px;top:33px;font-family:"Raleway",sans-serif;font-weight:700;font-size:21px;color:var(--ink);white-space:nowrap}
.title-rule{position:absolute;left:45px;top:66px;width:26px;height:3px;background:var(--green)}
.footnote{position:absolute;font-size:6px;color:#8a8a8a}

.body-copy{position:absolute;left:50px;top:100px;width:492px;font-size:6.3px;line-height:8px;color:#555}
.body-copy p{margin-bottom:7px}

.pie-heading{position:absolute;left:300px;top:122px;font-family:"Raleway",sans-serif;font-weight:700;font-size:27px;color:var(--ink)}
.pie-sub{position:absolute;left:300px;top:166px;font-weight:600;font-style:italic;font-size:10px;color:var(--green)}
.pie-copy{position:absolute;left:300px;top:184px;width:235px;font-size:8.5px;line-height:11px;color:#555}

.returns{position:absolute;left:58px;top:101px;display:grid;grid-template-columns:59px 96px 105px 105px 112px;grid-auto-rows:13.7px;font-size:7.5px}
.returns div{display:flex;align-items:center;justify-content:center}
.returns .yr{justify-content:flex-end;padding-right:10px;color:#333}
.returns .hd{background:var(--green);color:#fff;font-size:6.5px;font-weight:700;height:11px;align-self:start}
.returns .hd2{background:#9c9c9c;color:#fff;font-size:6px;font-weight:700;height:11px;align-self:start}
.returns .v{background:var(--cell-green);color:#2f2f2f}
.returns .neg{background:var(--cell-pink);color:#9c0006}
.returns-name{position:absolute;left:160px;top:86px;font-size:7.5px;font-weight:700;color:#333}

.stats{position:absolute;left:46px;top:85px;display:grid;grid-template-columns:289px 105px 104px;font-size:6.5px}
.stats .h{height:28px;display:flex;align-items:center;justify-content:center;color:#fff;font-weight:700;font-size:7.5px;text-align:center;line-height:9px}
.stats .h-label,.stats .h-fund{background:var(--grey)}
.stats .h-bench{background:var(--green)}
.stats .c{height:13.1px;display:flex;align-items:center;border-bottom:1px solid #f0f0f0;color:#222}
.stats .lbl{font-weight:700;padding-left:3px}
.stats .fund{justify-content:center;background:var(--cell-grey)}
.stats .bench{justify-content:center}

.disclaimer-title{position:absolute;left:45px;top:38px;font-family:"Raleway",sans-serif;font-weight:700;font-size:32px;color:var(--ink)}
.disclaimer-rule{position:absolute;left:45px;top:80px;width:26px;height:3px;background:var(--green)}
.disclaimer-copy{position:absolute;left:49px;top:92px;width:495px;font-size:6.7px;line-height:9.6px;text-align:justify;color:#555}

svg text{font-family:"Open Sans",Arial,sans-serif}
</style>
</head>
<body>
<main class="deck">

<section class="slide">
  <div class="brand-block" style="left:0;top:0;width:585px;height:252px;background:var(--grey)"></div>
  <h1 class="cover-title" style="left:46px;top:80px;font-size:22px;line-height:26px">Independent<br>Financial Advisory<br>Services Tailored To<br>Your Goals</h1>
  <p class="cover-date" style="left:48px;top:190px">ABC, XYZ – April 2021</p>
  <div class="brand-block" style="left:355px;top:49px;width:165px;height:164px;background:var(--green)"></div>
  <div class="lockup lockup--center" style="top:270px"><span class="lockup__mark"></span><span class="lockup__name">VANTERRA</span></div>
</section>

<section class="slide">
  <div class="lockup" style="left:36px;top:56px"><span class="lockup__mark"></span><span class="lockup__name" style="font-size:11px">VANTERRA</span></div>
  <h1 class="cover-title cover-title--dark" style="left:36px;top:104px;font-size:22px;line-height:26px">Independent<br>Financial Advisory<br>Services Tailored<br>To Your Goals</h1>
  <p class="cover-date cover-date--dark" style="left:38px;top:218px">ABC, XYZ – April 2021</p>
  <div class="brand-block" style="left:302px;top:46px;width:241px;height:240px;background:var(--green)"></div>
</section>

<section class="slide slide--green">
  <h1 class="cover-title" style="left:37px;top:104px;font-size:22px;line-height:26px">Independent<br>Financial Advisory<br>Services Tailored<br>To Your Goals</h1>
  <p class="cover-date" style="left:40px;top:218px">ABC, XYZ – April 2021</p>
  <div class="brand-block" style="left:304px;top:51px;width:232px;height:233px;background:#fff"></div>
</section>

<section class="slide slide--grey">
  <div class="bar-top"></div>
  <div class="lockup lockup--center" style="top:68px"><span class="lockup__mark"></span><span class="lockup__name">VANTERRA</span></div>
  <h1 class="cover-title" style="left:0;right:0;top:121px;text-align:center;font-size:28px;line-height:31px">Independent Financial<br>Advisory Services<br>Tailored To Your Goals</h1>
  <p class="cover-date" style="left:0;right:0;top:226px;text-align:center">ABC, XYZ – April 2021</p>
  <div class="bar-bottom"></div>
</section>

<section class="slide slide--grey">
  <div class="lockup lockup--center" style="top:68px"><span class="lockup__mark"></span><span class="lockup__name">VANTERRA</span></div>
  <h1 class="cover-title" style="left:0;right:0;top:121px;text-align:center;font-size:28px;line-height:31px">Independent Financial<br>Advisory Services<br>Tailored To Your Goals</h1>
  <p class="cover-date" style="left:0;right:0;top:226px;text-align:center">ABC, XYZ – April 2021</p>
</section>

<section class="slide">
  <div class="lockup" style="left:43px;top:62px"><span class="lockup__mark"></span><span class="lockup__name" style="font-size:11px">VANTERRA</span></div>
  <h1 class="cover-title cover-title--dark" style="left:42px;top:108px;font-size:25px;line-height:29px">Independent Financial<br>Advisory Services<br>Tailored To Your Goals</h1>
  <p class="cover-date cover-date--dark" style="left:46px;top:201px">ABC, XYZ – April 2021</p>
  <svg class="fill" viewBox="0 0 585 329" aria-hidden="true">
    <polyline points="60,288 116,288 176,288 239,288 301,283 353,264 402,233 448,184 493,113 526,43" fill="none" stroke="var(--green)" stroke-width="3"/>
    <g fill="var(--green)">
      <rect x="55" y="283" width="10" height="10"/><rect x="111" y="283" width="10" height="10"/><rect x="171" y="283" width="10" height="10"/><rect x="234" y="283" width="10" height="10"/><rect x="294.5" y="276.5" width="13" height="13"/><rect x="345" y="256" width="16" height="16"/><rect x="392" y="223" width="20" height="20"/><rect x="436" y="172" width="24" height="24"/><rect x="479" y="99" width="28" height="28"/><rect x="510" y="27" width="32" height="32"/>
    </g>
  </svg>
  <div class="bar-bottom"></div>
</section>

<section class="slide">
  <div class="lockup" style="left:43px;top:62px"><span class="lockup__mark"></span><span class="lockup__name" style="font-size:11px">VANTERRA</span></div>
  <h1 class="cover-title cover-title--dark" style="left:42px;top:108px;font-size:25px;line-height:29px">Independent Financial<br>Advisory Services<br>Tailored To Your Goals</h1>
  <p class="cover-date cover-date--dark" style="left:46px;top:201px">ABC, XYZ – April 2021</p>
  <svg class="fill" viewBox="0 0 585 329" aria-hidden="true">
    <polyline points="60,288 116,288 176,288 239,288 301,283 353,264 402,233 448,184 493,113 526,43" fill="none" stroke="var(--green)" stroke-width="3"/>
    <g fill="var(--green)">
      <rect x="55" y="283" width="10" height="10"/><rect x="111" y="283" width="10" height="10"/><rect x="171" y="283" width="10" height="10"/><rect x="234" y="283" width="10" height="10"/><rect x="294.5" y="276.5" width="13" height="13"/><rect x="345" y="256" width="16" height="16"/><rect x="392" y="223" width="20" height="20"/><rect x="436" y="172" width="24" height="24"/><rect x="479" y="99" width="28" height="28"/><rect x="510" y="27" width="32" height="32"/>
    </g>
  </svg>
  <div class="bar-bottom"></div>
</section>

<section class="slide slide--grey">
  <div class="lockup" style="left:43px;top:62px"><span class="lockup__mark"></span><span class="lockup__name" style="font-size:11px">VANTERRA</span></div>
  <h1 class="cover-title" style="left:42px;top:108px;font-size:25px;line-height:29px">Independent Financial<br>Advisory Services<br>Tailored To Your Goals</h1>
  <p class="cover-date" style="left:46px;top:201px">ABC, XYZ – April 2021</p>
  <svg class="fill" viewBox="0 0 585 329" aria-hidden="true">
    <polyline points="60,288 116,288 176,288 239,288 301,283 353,264 402,233 448,184 493,113 526,43" fill="none" stroke="var(--green)" stroke-width="3"/>
    <g fill="var(--green)">
      <rect x="55" y="283" width="10" height="10"/><rect x="111" y="283" width="10" height="10"/><rect x="171" y="283" width="10" height="10"/><rect x="234" y="283" width="10" height="10"/><rect x="294.5" y="276.5" width="13" height="13"/><rect x="345" y="256" width="16" height="16"/><rect x="392" y="223" width="20" height="20"/><rect x="436" y="172" width="24" height="24"/><rect x="479" y="99" width="28" height="28"/><rect x="510" y="27" width="32" height="32"/>
    </g>
  </svg>
  <div class="bar-bottom"></div>
</section>

<section class="slide">
  <span class="corner-mark"></span>
  <p class="confidential">Private and Confidential – Not for Distribution</p>
  <span class="page-no">9</span>
</section>

<section class="slide">
  <span class="corner-mark"></span>
  <p class="confidential">Private and Confidential – Not for Distribution</p>
  <h2 class="slide-title" style="left:49px;top:46px;font-size:26px">Simple Text Slide</h2>
  <div class="body-copy">
    <p>Lorem ipsum dolor sit amet, consectetur adipiscing elit, sed do eiusmod tempor incididunt ut labore et dolore magna aliqua. Lorem ipsum dolor sit amet, consectetur adipiscing elit, sed do eiusmod tempor incididunt ut labore et dolore magna aliqua. Ut enim ad minim veniam, quis nostrud exercitation ullamco laboris nisi ut aliquip.</p>
    <p>Lorem ipsum dolor sit amet, consectetur adipiscing elit, sed do eiusmod tempor incididunt ut labore et dolore magna aliqua. Lorem ipsum dolor sit amet, consectetur adipiscing elit, sed do eiusmod tempor incididunt ut labore et dolore magna aliqua. Ut enim ad minim veniam, quis nostrud exercitation ullamco laboris nisi ut aliquip. Lorem ipsum dolor sit amet, consectetur adipiscing elit, sed do eiusmod tempor incididunt ut labore et dolore magna aliqua. Lorem ipsum dolor sit amet, consectetur adipiscing elit, sed do eiusmod tempor incididunt ut labore et dolore magna aliqua. Ut enim ad minim veniam, quis nostrud exercitation ullamco laboris nisi ut aliquip.</p>
    <p>Lorem ipsum dolor sit amet, consectetur adipiscing elit, sed do eiusmod tempor incididunt ut labore et dolore magna aliqua. Lorem ipsum dolor sit amet, consectetur adipiscing elit, sed do eiusmod tempor incididunt ut labore et dolore magna aliqua. Ut enim ad minim veniam, quis nostrud exercitation ullamco laboris nisi ut aliquip. Lorem ipsum dolor sit amet, consectetur adipiscing elit, sed do eiusmod tempor incididunt ut labore et dolore magna aliqua. Lorem ipsum dolor sit amet, consectetur adipiscing elit, sed do eiusmod tempor incididunt ut labore et dolore magna aliqua. Ut enim ad minim veniam, quis nostrud exercitation ullamco laboris nisi ut aliquip.</p>
    <p>Lorem ipsum dolor sit amet, consectetur adipiscing elit, sed do eiusmod tempor incididunt ut labore et dolore magna aliqua. Lorem ipsum dolor sit amet, consectetur adipiscing elit, sed do eiusmod tempor incididunt ut labore et dolore magna aliqua. Ut enim ad minim veniam, quis nostrud exercitation ullamco laboris nisi ut aliquip.</p>
  </div>
  <span class="page-no">10</span>
</section>

<section class="slide">
  <span class="corner-mark"></span>
  <p class="confidential">Private and Confidential – Not for Distribution</p>
  <svg class="fill" viewBox="0 0 585 329" role="img" aria-label="Pie chart: 64% first quarter, 25% second quarter, 11% third quarter">
    <ellipse cx="147" cy="175" rx="66" ry="66" fill="var(--green-dark)"/>
    <path d="M147,167 L147,101 A66,66 0 1 1 96.2,209.1 Z" fill="var(--green)"/>
    <path d="M147,167 L96.2,209.1 A66,66 0 0 1 105,116.2 Z" fill="var(--grey)"/>
    <path d="M147,167 L105,116.2 A66,66 0 0 1 147,101 Z" fill="#111"/>
    <text x="130" y="124" font-size="9" font-weight="700" fill="#fff" text-anchor="middle">11%</text>
    <text x="103" y="160" font-size="9" font-weight="700" fill="#fff" text-anchor="middle">25%</text>
    <text x="186" y="192" font-size="9" font-weight="700" fill="#fff" text-anchor="middle">64%</text>
    <g font-size="6" fill="#666">
      <rect x="108" y="273" width="4" height="4" fill="var(--green)"/><text x="114" y="277.5">1st Qtr</text>
      <rect x="140" y="273" width="4" height="4" fill="var(--grey)"/><text x="146" y="277.5">2nd Qtr</text>
      <rect x="174" y="273" width="4" height="4" fill="#111"/><text x="180" y="277.5">3rd Qtr</text>
    </g>
  </svg>
  <h2 class="pie-heading">Pie Chart</h2>
  <p class="pie-sub">Lorem ipsum dolor sit amet</p>
  <p class="pie-copy">Lorem ipsum dolor sit amet, consectetur adipiscing elit, sed do eiusmod tempor incididunt ut labore et dolore magna aliqua. Lorem ipsum dolor sit amet, consectetur adipiscing elit. Lorem ipsum dolor sit amet, consectetur adipiscing elit, sed do eiusmod tempor incididunt ut labore et dolore magna aliqua.</p>
  <span class="page-no">11</span>
</section>

<section class="slide">
  <span class="corner-mark"></span>
  <p class="confidential">Private and Confidential – Not for Distribution</p>
  <h2 class="slide-title">ABC, XYZ – Growth of $1,000 vs Benchmark*</h2>
  <div class="title-rule"></div>
  <svg class="fill" viewBox="0 0 585 329" role="img" aria-label="Line chart of growth of $1,000 for ABC, XYZ, hedge funds and benchmark">
    <g stroke="var(--grid)" stroke-width=".6">
      <line x1="102" y1="83" x2="510" y2="83"/><line x1="102" y1="108" x2="510" y2="108"/><line x1="102" y1="133" x2="510" y2="133"/><line x1="102" y1="158" x2="510" y2="158"/><line x1="102" y1="184" x2="510" y2="184"/><line x1="102" y1="209" x2="510" y2="209"/><line x1="102" y1="234" x2="510" y2="234"/><line x1="102" y1="259" x2="510" y2="259"/>
    </g>
    <g font-size="5.5" fill="#777" text-anchor="end">
      <text x="96" y="85">$3,500</text><text x="96" y="110">$3,000</text><text x="96" y="135">$2,500</text><text x="96" y="160">$2,000</text><text x="96" y="186">$1,500</text><text x="96" y="211">$1,000</text><text x="96" y="236">$500</text><text x="96" y="261">$-</text>
    </g>
    <g font-size="4.5" fill="#888" text-anchor="end">
      <text transform="translate(104,265) rotate(-90)">Jan-12</text><text transform="translate(145,265) rotate(-90)">Jan-13</text><text transform="translate(186,265) rotate(-90)">Jan-14</text><text transform="translate(227,265) rotate(-90)">Jan-15</text><text transform="translate(267,265) rotate(-90)">Jan-16</text><text transform="translate(308,265) rotate(-90)">Jan-17</text><text transform="translate(349,265) rotate(-90)">Jan-18</text><text transform="translate(390,265) rotate(-90)">Jan-19</text><text transform="translate(431,265) rotate(-90)">Jan-20</text><text transform="translate(471,265) rotate(-90)">Jan-21</text><text transform="translate(510,265) rotate(-90)">Apr-21</text>
    </g>
    <g fill="none" stroke-width="1.3">
      <polyline stroke="var(--line-yellow)" points="102,208.7 122.4,209.2 142.8,211.2 163.2,209.7 183.6,207.7 204,208.7 224.4,206.2 244.8,205.2 265.2,204.7 285.6,206.2 306,203.7 326.4,201.2 346.8,202.7 367.2,199.7 387.6,197.6 408,194.6 428.4,191.1 448.8,186.1 469.2,178.5 489.6,171 510,159.9"/>
      <polyline stroke="var(--line-bench)" points="102,208.7 122.4,208.7 142.8,210.7 163.2,207.7 183.6,205.7 204,206.7 224.4,203.7 244.8,202.2 265.2,200.7 285.6,201.7 306,197.1 326.4,194.1 346.8,195.6 367.2,191.6 387.6,188.6 408,185.1 428.4,181 448.8,176 469.2,166 489.6,155.9 510,146.9"/>
      <polyline stroke="var(--line-blue)" points="102,208.7 122.4,208.2 142.8,209.2 163.2,206.2 183.6,203.7 204,204.7 224.4,201.2 244.8,198.7 265.2,197.1 285.6,197.6 306,192.6 326.4,188.6 346.8,189.6 367.2,184.6 387.6,181 408,176 428.4,171 448.8,163.4 469.2,153.4 489.6,143.3 510,131.4"/>
      <polyline stroke="#a8d05a" points="102,208.7 122.4,207.7 142.8,209.7 163.2,204.7 183.6,201.2 204,202.7 224.4,196.1 244.8,193.6 265.2,189.6 285.6,191.1 306,183.6 326.4,178.5 346.8,181 367.2,173.5 387.6,168.5 408,163.4 428.4,155.9 448.8,148.4 469.2,135.8 489.6,118.2 510,96.7"/>
    </g>
    <g font-size="5.5" fill="#666" text-anchor="end">
      <text x="508" y="90">ABC $3,228</text>
      <text x="500" y="124">Hedge Funds 50/50 $2,537</text>
      <text x="500" y="141">Benchmark $2,228</text>
      <text x="506" y="174">XYZ $1,971</text>
    </g>
  </svg>
  <p class="footnote" style="left:83px;top:296px">Benchmark = 45% xxxxxxxx, 15% yyyyyyyy, 40% zzzzzzzz</p>
  <span class="page-no">12</span>
</section>

<section class="slide">
  <span class="corner-mark"></span>
  <p class="confidential">Private and Confidential – Not for Distribution</p>
  <h2 class="slide-title">ABC, XYZ – Annual Returns vs Benchmark*</h2>
  <div class="title-rule"></div>
  <p class="returns-name">LINDELL</p>
  <div class="returns">
    <div></div><div class="hd">60/40</div><div class="hd">Alder</div><div class="hd">Northgate</div><div class="hd">50/50</div>
    <div></div><div class="hd2">BENCHMARK</div><div class="hd2">CREEK</div><div class="hd2">COMPOSITE</div><div class="hd2">HEDGE FUNDS</div>
    <div class="yr">2011</div><div class="v">0.6%</div><div class="v">4.6%</div><div class="v">4.8%</div><div class="v">4.7%</div>
    <div class="yr">2012</div><div class="v">11.3%</div><div class="v">10.5%</div><div class="v">14.5%</div><div class="v">12.5%</div>
    <div class="yr">2013</div><div class="v">16.0%</div><div class="v">8.2%</div><div class="v">12.3%</div><div class="v">10.2%</div>
    <div class="yr">2014</div><div class="v">6.1%</div><div class="neg">-2.5%</div><div class="v">15.5%</div><div class="v">6.5%</div>
    <div class="yr">2015</div><div class="neg">-0.1%</div><div class="neg">-1.7%</div><div class="v">14.6%</div><div class="v">6.5%</div>
    <div class="yr">2016</div><div class="v">7.2%</div><div class="v">4.6%</div><div class="v">5.7%</div><div class="v">5.2%</div>
    <div class="yr">2017</div><div class="v">13.9%</div><div class="v">9.2%</div><div class="v">10.4%</div><div class="v">9.8%</div>
    <div class="yr">2018</div><div class="neg">-3.8%</div><div class="v">6.6%</div><div class="v">11.3%</div><div class="v">9.0%</div>
    <div class="yr">2019</div><div class="v">19.3%</div><div class="v">7.7%</div><div class="v">10.7%</div><div class="v">9.2%</div>
    <div class="yr">2020</div><div class="v">12.1%</div><div class="v">15.8%</div><div class="v">19.6%</div><div class="v">17.7%</div>
    <div class="yr">YTD 2021</div><div class="v">2.5%</div><div class="v">8.2%</div><div class="v">5.1%</div><div class="v">6.7%</div>
  </div>
  <p class="footnote" style="left:0;right:0;top:286px;text-align:center;padding-left:50px">Benchmark = 45% xxxxxxxx, 15% yyyyyyyy, 40% zzzzzzzz</p>
  <span class="page-no">13</span>
</section>

<section class="slide">
  <span class="corner-mark"></span>
  <p class="confidential">Private and Confidential – Not for Distribution</p>
  <h2 class="slide-title">ABC, XYZ – Risk / Return vs Benchmark*</h2>
  <div class="title-rule"></div>
  <svg class="fill" viewBox="0 0 585 329" role="img" aria-label="Scatter chart of return against standard deviation">
    <g stroke="var(--grid)" stroke-width=".6">
      <line x1="79" y1="76" x2="523" y2="76"/><line x1="79" y1="98" x2="523" y2="98"/><line x1="79" y1="121" x2="523" y2="121"/><line x1="79" y1="143" x2="523" y2="143"/><line x1="79" y1="165" x2="523" y2="165"/><line x1="79" y1="187" x2="523" y2="187"/><line x1="79" y1="210" x2="523" y2="210"/><line x1="79" y1="232" x2="523" y2="232"/><line x1="79" y1="254" x2="523" y2="254"/>
      <line x1="79" y1="76" x2="79" y2="254"/><line x1="134.5" y1="76" x2="134.5" y2="254"/><line x1="190" y1="76" x2="190" y2="254"/><line x1="245.5" y1="76" x2="245.5" y2="254"/><line x1="301" y1="76" x2="301" y2="254"/><line x1="356.5" y1="76" x2="356.5" y2="254"/><line x1="412" y1="76" x2="412" y2="254"/><line x1="467.5" y1="76" x2="467.5" y2="254"/><line x1="523" y1="76" x2="523" y2="254"/>
    </g>
    <g font-size="5.5" fill="#888" text-anchor="end">
      <text x="74" y="78">16.0%</text><text x="74" y="100">14.0%</text><text x="74" y="123">12.0%</text><text x="74" y="145">10.0%</text><text x="74" y="167">8.0%</text><text x="74" y="189">6.0%</text><text x="74" y="212">4.0%</text><text x="74" y="234">2.0%</text><text x="74" y="256">0.0%</text>
    </g>
    <g font-size="5.5" fill="#888" text-anchor="middle">
      <text x="79" y="263">0.0%</text><text x="134.5" y="263">2.0%</text><text x="190" y="263">4.0%</text><text x="245.5" y="263">6.0%</text><text x="301" y="263">8.0%</text><text x="356.5" y="263">10.0%</text><text x="412" y="263">12.0%</text><text x="467.5" y="263">14.0%</text><text x="523" y="263">16.0%</text>
    </g>
    <rect x="41" y="118" width="11" height="92" rx="5.5" fill="var(--grey)"/>
    <text transform="translate(49,164) rotate(-90)" font-size="6" fill="#fff" text-anchor="middle">Return</text>
    <rect x="237" y="268" width="85" height="11" rx="5.5" fill="var(--grey)"/>
    <text x="279.5" y="276" font-size="6" fill="#fff" text-anchor="middle">Standard Deviation</text>
    <g font-size="6" fill="#555">
      <circle cx="195.6" cy="119.4" r="1.8" fill="#c0392b"/><text x="200" y="121.5">Northgate</text>
      <circle cx="162" cy="149.4" r="1.8" fill="#c0392b"/><text x="166" y="151.5">Hedge Funds 50/50</text>
      <circle cx="176" cy="178.4" r="1.8" fill="#2c3e90"/><text x="180" y="180.5">Alder Creek</text>
      <circle cx="312" cy="164" r="1.8" fill="#16a085"/><text x="316" y="166">60/40 Benchmark</text>
      <circle cx="465" cy="104" r="1.8" fill="var(--line-blue)"/><text x="440" y="92">Broad Equity Index</text>
      <circle cx="492" cy="198.4" r="1.8" fill="#7d3c98"/><text x="430" y="189">World ex Home Index</text>
      <circle cx="143" cy="226" r="1.8" fill="#b7950b"/><text x="147" y="230">Govt / Credit Bonds Index</text>
    </g>
  </svg>
  <p class="footnote" style="left:52px;top:294px">Benchmark = 45% xxxxxxxx, 15% yyyyyyyy, 40% zzzzzzzz</p>
  <span class="page-no">14</span>
</section>

<section class="slide">
  <span class="corner-mark"></span>
  <p class="confidential">Private and Confidential – Not for Distribution</p>
  <h2 class="slide-title">ABC, XYZ – analytical data vs Benchmark*</h2>
  <div class="title-rule"></div>
  <div class="stats">
    <div class="h h-label"></div><div class="h h-fund">50/50<br>Hedge Funds</div><div class="h h-bench">Benchmark</div>
    <div class="c lbl">Annualized Return</div><div class="c fund">9.5%</div><div class="c bench">8.1%</div>
    <div class="c lbl">Standard Deviation</div><div class="c fund">2.9%</div><div class="c bench">8.3%</div>
    <div class="c lbl">Average monthly return</div><div class="c fund">0.8%</div><div class="c bench">0.7%</div>
    <div class="c lbl">Largest monthly gain</div><div class="c fund">9.6%</div><div class="c bench">7.7%</div>
    <div class="c lbl">Largest monthly loss</div><div class="c fund">-2.5%</div><div class="c bench">-8.6%</div>
    <div class="c lbl">Max drawdown (consecutive negative months)</div><div class="c fund">-2.5%</div><div class="c bench">-12.5%</div>
    <div class="c lbl">% months of positive returns</div><div class="c fund">86%</div><div class="c bench">72%</div>
    <div class="c lbl">max # of months of consecutive loss</div><div class="c fund">2 (twice)</div><div class="c bench">5 (once)</div>
    <div class="c lbl">Monthly standard deviation</div><div class="c fund">0.8%</div><div class="c bench">2.4%</div>
    <div class="c lbl">Min annual return with 99% probability</div><div class="c fund">3.7%</div><div class="c bench">-8.5%</div>
    <div class="c lbl">% years outperformed 60/40 benchmark</div><div class="c fund">60%</div><div class="c bench"></div>
    <div class="c lbl">% months outperformed 60/40 benchmark</div><div class="c fund">65%</div><div class="c bench"></div>
    <div class="c lbl">R Square against benchmark</div><div class="c fund">8%</div><div class="c bench">100%</div>
  </div>
  <span class="page-no">15</span>
</section>

<section class="slide">
  <span class="corner-mark"></span>
  <p class="confidential">Private and Confidential – Not for Distribution</p>
  <h2 class="slide-title">ABC, XYZ vs Benchmark* – monthly volatility</h2>
  <svg class="fill" viewBox="0 0 585 329" role="img" aria-label="Bar chart of monthly returns for ABC, XYZ and benchmark">
    <g font-size="5" fill="#888" text-anchor="end">
      <text x="72" y="93">10.0%</text><text x="72" y="111">8.0%</text><text x="72" y="129">6.0%</text><text x="72" y="147">4.0%</text><text x="72" y="165">2.0%</text><text x="72" y="183">0.0%</text><text x="72" y="201">-2.0%</text><text x="72" y="219">-4.0%</text><text x="72" y="237">-6.0%</text><text x="72" y="255">-8.0%</text><text x="72" y="273">-10.0%</text>
    </g>
    <line x1="76" y1="181" x2="528" y2="181" stroke="#ccc" stroke-width=".6"/>
    <path stroke="var(--line-blue)" stroke-width="1.3" fill="none" d="M80 181v-12M90 181v8M100 181v-20M110 181v15M120 181v-6M130 181v-25M140 181v10M150 181v-14M160 181v22M170 181v-8M180 181v-30M190 181v12M200 181v-10M210 181v18M220 181v-16M230 181v6M240 181v-22M250 181v28M260 181v-9M270 181v-12M280 181v14M290 181v-26M300 181v9M310 181v-15M320 181v20M330 181v-7M340 181v-18M350 181v24M360 181v-11M370 181v8M380 181v-28M390 181v16M400 181v-13M410 181v11M420 181v-19M430 181v30M440 181v-8M450 181v12M460 181v-24M470 181v66M480 181v-10M490 181v15M500 181v-17M510 181v9M520 181v-14"/>
    <path stroke="var(--line-orange)" stroke-width="1.3" fill="none" d="M83 181v-8M93 181v5M103 181v-12M113 181v9M123 181v-4M133 181v-15M143 181v6M153 181v-9M163 181v14M173 181v-5M183 181v-18M193 181v8M203 181v-6M213 181v11M223 181v-10M233 181v4M243 181v-13M253 181v17M263 181v-6M273 181v-7M283 181v9M293 181v-16M303 181v5M313 181v-9M323 181v12M333 181v-4M343 181v-11M353 181v15M363 181v-7M373 181v5M383 181v-17M393 181v10M403 181v-8M413 181v7M423 181v-12M433 181v18M443 181v-5M453 181v7M463 181v-15M473 181v30M483 181v-6M493 181v9M503 181v-10M513 181v6M523 181v-9"/>
    <path stroke="var(--line-greybar)" stroke-width="1.3" fill="none" d="M86 181v-4M96 181v3M106 181v-6M116 181v4M126 181v-2M136 181v-7M146 181v3M156 181v-4M166 181v6M176 181v-2M186 181v-8M196 181v4M206 181v-3M216 181v5M226 181v-5M236 181v2M246 181v-6M256 181v8M266 181v-3M276 181v-3M286 181v4M296 181v-7M306 181v2M316 181v-4M326 181v5M336 181v-2M346 181v-5M356 181v7M366 181v-3M376 181v2M386 181v-8M396 181v5M406 181v-4M416 181v3M426 181v-6M436 181v8M446 181v-2M456 181v3M466 181v-7M476 181v12M486 181v-3M496 181v4M506 181v-5M516 181v3M526 181v-4"/>
    <g font-size="4.5" fill="#888" text-anchor="end">
      <text transform="translate(83,178) rotate(-90)">Jan-14</text><text transform="translate(123,178) rotate(-90)">May-14</text><text transform="translate(163,178) rotate(-90)">Sep-14</text><text transform="translate(203,178) rotate(-90)">Jan-15</text><text transform="translate(243,178) rotate(-90)">May-15</text><text transform="translate(283,178) rotate(-90)">Sep-15</text><text transform="translate(323,178) rotate(-90)">Jan-16</text><text transform="translate(363,178) rotate(-90)">May-16</text><text transform="translate(403,178) rotate(-90)">Sep-16</text><text transform="translate(443,178) rotate(-90)">Jan-17</text><text transform="translate(483,178) rotate(-90)">May-17</text><text transform="translate(523,178) rotate(-90)">Sep-17</text>
    </g>
  </svg>
  <span class="page-no">16</span>
</section>

<section class="slide">
  <span class="corner-mark"></span>
  <p class="confidential">Private and Confidential – Not for Distribution</p>
  <h2 class="slide-title">ABC, XYZ – Return distribution</h2>
  <div class="title-rule"></div>
  <svg class="fill" viewBox="0 0 585 329" role="img" aria-label="Histogram of ABC, XYZ monthly return distribution">
    <rect x="39" y="92" width="512" height="215" rx="3" fill="#fff" stroke="#ececec"/>
    <g stroke="var(--grid)" stroke-width=".5">
      <line x1="62" y1="105" x2="535" y2="105"/><line x1="62" y1="125.4" x2="535" y2="125.4"/><line x1="62" y1="145.9" x2="535" y2="145.9"/><line x1="62" y1="166.3" x2="535" y2="166.3"/><line x1="62" y1="186.8" x2="535" y2="186.8"/><line x1="62" y1="207.2" x2="535" y2="207.2"/><line x1="62" y1="227.7" x2="535" y2="227.7"/><line x1="62" y1="248.1" x2="535" y2="248.1"/><line x1="62" y1="268.6" x2="535" y2="268.6"/><line x1="62" y1="289" x2="535" y2="289"/>
    </g>
    <g font-size="5.5" fill="#777" text-anchor="end">
      <text x="58" y="107">45</text><text x="58" y="127">40</text><text x="58" y="148">35</text><text x="58" y="168">30</text><text x="58" y="189">25</text><text x="58" y="209">20</text><text x="58" y="230">15</text><text x="58" y="250">10</text><text x="58" y="271">5</text><text x="58" y="291">0</text>
    </g>
    <g fill="var(--green)" stroke="#fff" stroke-width=".8">
      <rect x="64" y="284.9" width="36" height="4.1"/><rect x="100" y="284.9" width="36" height="4.1"/><rect x="208" y="252.2" width="36" height="36.8"/><rect x="244" y="178.6" width="36" height="110.4"/><rect x="280" y="129.5" width="36" height="159.5"/><rect x="316" y="154" width="36" height="135"/><rect x="352" y="260.4" width="36" height="28.6"/><rect x="388" y="272.6" width="36" height="16.4"/><rect x="424" y="284.9" width="36" height="4.1"/><rect x="496" y="284.9" width="36" height="4.1"/>
    </g>
    <g font-size="4.2" fill="#666" text-anchor="middle">
      <text x="82" y="298">(-2.5%,-1.9%]</text><text x="118" y="298">(-1.9%,-1.3%]</text><text x="154" y="298">(-1.3%,-0.7%]</text><text x="190" y="298">(-0.7%,-0.1%]</text><text x="226" y="298">(-0.1%,0.5%]</text><text x="262" y="298">(0.5%,1.1%]</text><text x="298" y="298">(1.1%,1.7%]</text><text x="334" y="298">(1.7%,2.3%]</text><text x="370" y="298">(2.3%,2.9%]</text><text x="406" y="298">(2.9%,3.5%]</text><text x="442" y="298">(3.5%,4.1%]</text><text x="478" y="298">(4.1%,4.7%]</text><text x="514" y="298">(4.7%,5.3%]</text>
    </g>
  </svg>
  <span class="page-no">17</span>
</section>

<section class="slide">
  <span class="corner-mark"></span>
  <p class="confidential">Private and Confidential – Not for Distribution</p>
  <h2 class="slide-title" style="left:46px;top:31px">Benchmark* – Return distribution</h2>
  <div class="title-rule" style="left:46px;top:63px"></div>
  <svg class="fill" viewBox="0 0 585 329" role="img" aria-label="Histogram of benchmark monthly return distribution">
    <g stroke="var(--grid)" stroke-width=".5">
      <line x1="66" y1="95.2" x2="536" y2="95.2"/><line x1="66" y1="137.4" x2="536" y2="137.4"/><line x1="66" y1="179.6" x2="536" y2="179.6"/><line x1="66" y1="221.8" x2="536" y2="221.8"/><line x1="66" y1="264" x2="536" y2="264"/>
    </g>
    <g font-size="5.5" fill="#777" text-anchor="end">
      <text x="62" y="97">40</text><text x="62" y="139">30</text><text x="62" y="182">20</text><text x="62" y="224">10</text><text x="62" y="266">0</text>
    </g>
    <g fill="var(--green)" stroke="#fff" stroke-width=".8">
      <rect x="68" y="261.9" width="46.7" height="2.1"/><rect x="114.7" y="261.9" width="46.7" height="2.1"/><rect x="161.4" y="242.9" width="46.7" height="21.1"/><rect x="208.1" y="247.1" width="46.7" height="16.9"/><rect x="254.8" y="175.4" width="46.7" height="88.6"/><rect x="301.5" y="99.4" width="46.7" height="164.6"/><rect x="348.2" y="171.2" width="46.7" height="92.8"/><rect x="394.9" y="242.9" width="46.7" height="21.1"/><rect x="441.6" y="261.9" width="46.7" height="2.1"/><rect x="488.3" y="255.6" width="46.7" height="8.4"/>
    </g>
    <g font-size="4.6" fill="#666" text-anchor="middle">
      <text x="91" y="273">(-8.6%,-6.9%]</text><text x="138" y="273">(-6.9%,-5.2%]</text><text x="185" y="273">(-5.2%,-3.5%]</text><text x="231" y="273">(-3.5%,-1.8%]</text><text x="278" y="273">(-1.8%,-0.1%]</text><text x="325" y="273">(-0.1%,1.6%]</text><text x="372" y="273">(1.6%,3.3%]</text><text x="418" y="273">(3.3%,5.0%]</text><text x="465" y="273">(5.0%,6.7%]</text><text x="512" y="273">(6.7%,8.4%]</text>
    </g>
  </svg>
  <span class="page-no">18</span>
</section>

<section class="slide">
  <span class="corner-mark"></span>
  <p class="confidential">Private and Confidential – Not for Distribution</p>
  <h2 class="disclaimer-title">Disclaimer</h2>
  <div class="disclaimer-rule"></div>
  <p class="disclaimer-copy">Disclaimer: this document is a general communication being provided for informational purposes only. It is educational in nature and not designed to be taken as advice or a recommendation for any specific investment product, strategy, plan feature or other purpose in any jurisdiction. Any examples used are generic, hypothetical and for illustration purposes only. This material does not contain sufficient information to support an investment decision and it should not be relied upon by you in evaluating the merits of investing in any securities or products. In addition, users should make an independent assessment of the legal, regulatory, tax, credit, and accounting implications and determine, together with their own professional advisers, if any investment mentioned herein is believed to be suitable to their personal goals. Investors should ensure that they obtain all available relevant information before making any investment. Any forecasts, figures, opinions or investment techniques and strategies set out are for information purposes only, based on certain assumptions and current market conditions and are subject to change without prior notice. All information presented herein is considered to be accurate at the time of production, but no warranty of accuracy is given and no liability in respect of any error or omission is accepted. It should be noted that investment involves risks, the value of investments and the income from them may fluctuate in accordance with market conditions and taxation agreements and investors may not get back the full amount invested. Both past performance and yields are not reliable indicators of current and future results.</p>
  <span class="page-no">19</span>
</section>

</main>
</body>
</html>
```